We need a mobile and desktop design for our new online store, Ripper Rustic. The website's goals is to help Australian manufacturers and inventors sell their goods online.

The site needs to match the them of our logo.
Updates

Reason: We are extending the deadline because we have been away for Easter and was unable to answer everyone's questions.

Thank you for everyone's questions. I'm sorry for the delay in my answer. I have been away. We do not need the site coded. My coders have asked for a graphic they can cut up.

While we don't need anyone to code the site. If the choosen designer does a great job and is easy to work with, it highly likely we will hire them for future work. We have been running a business online for ten years and are short a graphic designer at the moment. It is fair to think of this as the first stage of a job interview.

The target market is Australian consumers. The website is a marketing portal for Australian producers/manufacturers/inventors to sell their goods online.

We will be helping companies who are brilliant at making goods but need some help selling them online.

Each company will have it''s own store on the site. The companies lined up so far include a chocolate manufacturer, kitchen sponge manufacturer, curry producer and surfboard maker. The range of stores will vary. We are looking for an overall design to work from.

We are basins the function of the store design on BrainFizz.com store and our existing store you can view at www.tidypurse.com.au/store. I also like Green Kite days and Wombuy.com.au

I'm sorry, we are not going to guarantee payment. Just in case, none of the designs are appropriate. But, this is the third time we have used Pixel Gather and we paid for both previous jobs. We are not here to waste time.

If you have any more questions. Fire away. I''m sorry, my last brief was a bit too brief. It was my last task before rushing to a school presentation.

I'm looking forward to seeing everyone's designs and hopefully meeting a new designer.

Here is a link to our first mock up of the site created by our coders. Ignore the graphics and text. (It was the boys putting something there to work from.) The URL is:-

www.ripperrustic.com

The stores motto is...

"We only sell goods that are Ripper Rustic!"

Our goals are..

To help Australian manufacturers, inventors and producers. People who are good at making items and are adding value to Australia, but are so busy making their goods that they struggle selling them online.

Of the designs we have seen so far, I prefer the blue and white based designs, instead of the red adn white. Because, the red ones seem to make the site look more bloody then brilliant :-)

All businesses/stores will be given a Gold, Bronze or Silver ranking, depending on how much of their work benefits Australia.

Thank you for everyone's designs so far. The quality of the designs have been excellent! Our team will be discussing them on Thursday. I'll post an update on Friday morning

All the best,

Maree

Target Market(s)

Australians, general

Industry/Entity Type

Store

Requirements
Must have
• Online store

```html
<!DOCTYPE html>
<html lang="en">
<head>
<meta charset="utf-8">
<title>Ripper Rustic – Desktop and Smartphone</title>
<link href="https://fonts.googleapis.com/css2?family=Signika:wght@400;600;700&display=swap" rel="stylesheet">
<style>
:root{
  --blue:#0b9ad8;
  --blue-dark:#0878b0;
  --red:#8b1c1c;
  --page:#ebebeb;
  --ink:#1b1b1b;
  --text:#444;
  --white:#fff;
  --footer:#1f1f22;
  --footer-panel:#141416;
  --link:#2aa7e6;
}
*{box-sizing:border-box;margin:0;padding:0}
html,body{width:1200px;height:1200px;overflow:hidden;background:#fff}
body{font-family:"Signika",sans-serif;color:var(--ink)}
.stage{position:absolute;left:0;top:0;width:1390px;height:1390px;transform:scale(.8633);transform-origin:0 0}
.abs{position:absolute}
.label{font-size:15px;font-weight:600;color:var(--ink)}
.page{background:var(--page);overflow:hidden}
.photo{position:absolute}
.brand{display:flex;align-items:center;gap:8px;font-weight:700;color:var(--ink)}
.brand-dot{width:16px;height:16px;border-radius:50%;background:var(--blue)}
.nav{display:flex;align-items:center;gap:0;font-size:10px;color:var(--ink)}
.nav a{color:var(--ink);text-decoration:none;margin-right:22px}
.nav a.active{background:var(--blue);color:#fff;padding:6px 8px;border-radius:2px;margin-right:16px}
.tile{position:absolute;overflow:hidden}
.tile h3{font-weight:700;font-size:13px;line-height:1.3}
.tile p{font-size:9px;line-height:1.75}
.on-dark{color:#fff}
.more{position:absolute;background:var(--blue);color:#fff;font-size:9px;padding:5px 10px;border-radius:2px}
.blue{background:var(--blue);color:#fff}
.footer{background:var(--footer)}
.footer-panel{background:var(--footer-panel)}
.footer h4{color:#fff;font-size:13px;font-weight:600}
.footer p{color:#ddd;font-size:9.5px;line-height:1.8}
.footer .links a{display:block;color:var(--link);font-size:9.5px;line-height:1.8;text-decoration:none}
.load{display:flex;align-items:center;justify-content:center}
.m p{font-size:12.5px;line-height:1.6;color:var(--text)}
</style>
</head>
<body>
<div class="stage">

  <div class="abs label" style="left:59px;top:65px">Ripper Rustic / Desktop version</div>
  <div class="abs label" style="left:1057px;top:65px">Ripper Rustic / Smartphone version</div>

  <!-- DESKTOP -->
  <section class="abs page desktop" style="left:59px;top:96px;width:892px;height:1209px">
    <div class="abs brand" style="left:142px;top:100px;font-size:28px"><span class="brand-dot"></span>Ripper Rustic</div>
    <nav class="abs nav" style="left:490px;top:107px">
      <a class="active">Home</a><a>Store</a><a>Sell with us</a><a>About</a><a>Contact</a>
    </nav>

    <!-- hero -->
    <div class="photo" role="img" aria-label="Photo of a smiling woman in front of a warm striped backdrop" style="left:134px;top:204px;width:312px;height:163px;background:linear-gradient(90deg,#3a1c10,#8a5a32 35%,#c08a60 70%,#6a3a22)"></div>
    <div class="tile" style="left:134px;top:367px;width:312px;height:97px;background:var(--red);padding:6px 9px">
      <h3 class="on-dark" style="font-size:18px">Lena Marlowe starts E-commerce</h3>
      <p class="on-dark" style="font-size:9px;line-height:1.35;margin-top:4px">After years of waiting Lena Marlowe finally starts her own e-commerce with the help of Ripper Rustic. She sells her own Lena Marlowe fan stuff, everything from coffee cups to t-shirts. Have a look!</p>
      <svg class="abs" style="left:136px;top:86px" width="42" height="7"><circle cx="3.5" cy="3.5" r="3.5" fill="#e02020"/><circle cx="14" cy="3.5" r="3.5" fill="#b83232"/><circle cx="24.5" cy="3.5" r="3.5" fill="#b83232"/><circle cx="35" cy="3.5" r="3.5" fill="#b83232"/></svg>
    </div>

    <div class="tile" style="left:455px;top:204px;width:148px;height:260px;color:var(--text)">
      <h3 style="color:var(--ink)">Everything starts with an idea..</h3>
      <p style="margin-top:14px">We are Ripper Rustic and we help Australian manufacturers to sell online! Dolor sit amet, consectetur adipisicing elit, sed do eiusmod tempor incididunt ut.</p>
      <p style="margin-top:14px">Dolor sit amet, consectetur adipisicing elit, sed do eiusmod tempor incididunt ut. Dolor sit amet, consectetur adipisicing elit, sed do eiusmod tempor incididunt ut.</p>
    </div>

    <div class="tile blue" style="left:603px;top:334px;width:156px;height:130px;padding:6px">
      <h3 style="font-size:20px">03 April, 2013</h3>
      <p style="margin-top:12px">Today is the day the first cell phone call was made in 1973. The call itself took place in New York and the phones weight was about 1 kilo.</p>
    </div>

    <!-- row 2 -->
    <div class="tile" role="img" aria-label="Photo of a white computer mouse" style="left:134px;top:464px;width:156px;height:129px;background:linear-gradient(160deg,#9a9a9a,#d8d8d8 55%,#f5f5f5);padding:6px 8px">
      <h3 class="on-dark">This just in.</h3>
      <p class="on-dark" style="margin-top:28px;line-height:1.5">Orchard Glide Mouse, the new generation mouse.</p>
      <span class="more" style="right:8px;bottom:9px">More</span>
    </div>
    <div class="tile blue" style="left:290px;top:464px;width:156px;height:129px">
      <svg class="abs" style="left:6px;top:6px" width="40" height="20"><rect x="2" y="1" width="4" height="13" rx="2" fill="#111"/><circle cx="4" cy="15" r="3.5" fill="#111"/></svg>
      <div class="abs" style="left:18px;top:3px;font-size:19px;font-weight:700;color:var(--ink)">24°</div>
      <svg class="abs" style="left:42px;top:28px" width="75" height="65" viewBox="0 0 75 65">
        <g stroke="#111" stroke-width="4" stroke-linecap="round" fill="none">
          <line x1="40" y1="4" x2="40" y2="10"/><line x1="58" y1="10" x2="54" y2="15"/><line x1="66" y1="28" x2="60" y2="28"/><line x1="22" y1="10" x2="26" y2="15"/>
          <path d="M30 24a13 13 0 0 1 23 10"/>
          <path d="M16 56h30a11 11 0 0 0 0-22 15 15 0 0 0-28 5 9 9 0 0 0-2 17z"/>
        </g>
      </svg>
      <div class="abs" style="left:0;right:0;top:104px;text-align:center;font-size:9.5px;color:var(--ink)"><b>Sunny,</b> a bit cloudy</div>
    </div>
    <div class="tile" role="img" aria-label="Portrait photo of a smiling woman" style="left:446px;top:464px;width:157px;height:129px;background:linear-gradient(135deg,#2a2a2a,#5a4a44 55%,#1e1e1e);padding:6px 8px">
      <h3 class="on-dark">I sell with Ripper Rustic.</h3>
      <p class="on-dark" style="margin-top:24px">Cara Whitfield approves!</p>
      <span class="more" style="right:10px;bottom:9px">More</span>
    </div>
    <div class="tile" style="left:603px;top:464px;width:156px;height:129px;text-align:center">
      <h3 style="margin-top:12px">Like us on Chatterbook!</h3>
      <div class="abs" style="left:60px;top:38px;width:34px;height:34px;background:var(--blue);border-radius:3px"></div>
      <p style="position:absolute;left:0;right:0;top:86px;line-height:1.9;color:var(--ink)">Or, this is simply an invite<br>to play thumb wars..</p>
    </div>

    <!-- row 3 -->
    <div class="tile" role="img" aria-label="Black and white close-up photo of a man" style="left:134px;top:593px;width:156px;height:259px;background:linear-gradient(160deg,#111,#2e2e2e 50%,#777 80%,#2a2a2a);padding:26px 8px 0">
      <h3 class="on-dark">Questions?</h3>
      <p class="on-dark" style="margin-top:16px">We are live at 15.00 pm to answer any questions you might have.</p>
      <p class="on-dark" style="margin-top:14px">We will also stream a live webcam from our conference in New York so you guys can learn more about how to succeed with your e-commerce website.</p>
      <span class="more" style="right:10px;bottom:9px">More</span>
    </div>
    <div class="tile" style="left:290px;top:593px;width:156px;height:129px;padding:6px 8px;color:var(--text)">
      <h3 style="color:var(--ink)">It's so Ripper Rustic!</h3>
      <p style="margin-top:10px">What's your product? No matter what they all are brilliant and should therefore be treated as the million dollar idea...</p>
      <span class="more" style="right:9px;bottom:8px">More</span>
    </div>
    <div class="tile" role="img" aria-label="Video still of a film poster with a man's portrait" style="left:446px;top:593px;width:313px;height:129px;background:linear-gradient(90deg,#0c0c0c,#2a2a2a 45%,#6b5040 70%,#2a1a1a)">
      <svg class="abs" style="left:145px;top:45px" width="22" height="24"><path d="M2 2l18 10-18 10z" fill="#fff"/></svg>
      <div class="abs" style="left:140px;top:70px;font-size:13px;font-weight:700;color:#fff">PLAY</div>
    </div>

    <!-- row 4 -->
    <div class="tile" role="img" aria-label="Black and white photo of a man in costume" style="left:290px;top:722px;width:313px;height:130px;background:linear-gradient(90deg,#222,#3a3a3a 45%,#8a8a8a 70%,#1a1a1a);padding:6px 8px">
      <h3 class="on-dark">He's a Ripper Pirate! And he is Ripper Rustic.</h3>
      <p class="on-dark" style="margin-top:32px;line-height:1.7">Jack Danvers isn't the person that directly comes to mind when thinking about a webshop or e-commerce. Aaand, surprise! He starts his own with the help of Ripper Commerce.</p>
      <span class="more" style="right:12px;bottom:9px">More</span>
    </div>
    <div class="tile" style="left:603px;top:722px;width:156px;height:130px;padding:6px 8px">
      <h3 style="font-size:12.5px;line-height:1.38">I will always choose a lazy person to do a difficult job. Because, he will find an easy way to do it.</h3>
      <p style="margin-top:8px">- Will Harding</p>
    </div>

    <div class="abs load" style="left:367px;top:892px;width:160px;height:34px;background:#d8d8d8;color:#999;font-size:12px;border-bottom:2px solid #c4c4c4">Load more</div>

    <!-- footer -->
    <footer class="abs footer" style="left:0;top:993px;width:892px;height:216px">
      <div class="abs footer-panel" style="left:134px;top:13px;width:291px;height:190px"></div>
      <div class="abs footer-panel" style="left:445px;top:13px;width:314px;height:190px"></div>
      <h4 class="abs" style="left:148px;top:24px">Hey, over here!</h4>
      <p class="abs" style="left:148px;top:57px">58-60 Wattle St<br>Adelaide, SA 5000<br>Australia</p>
      <svg class="abs" style="left:148px;top:127px" width="14" height="30"><path d="M3 1c-2 1-2 4 0 7s5 5 8 4l1-2-3-2-1 1c-1 0-3-2-3-3l1-1-2-3z" fill="var(--link)"/><rect x="1" y="19" width="12" height="8" fill="var(--link)"/><path d="M1 19l6 5 6-5" stroke="var(--footer-panel)" fill="none"/></svg>
      <p class="abs" style="left:170px;top:124px">(08) 8000 4417<br>info@ripperrustic.com</p>
      <div class="abs" role="img" aria-label="Street map showing the office location" style="left:291px;top:25px;width:139px;height:167px;background:linear-gradient(180deg,#e6e2da,#dcd8ce);border:2px solid var(--blue)"></div>
      <h4 class="abs" style="left:469px;top:24px">Super fast links</h4>
      <div class="abs links" style="left:469px;top:57px"><a>Home</a><a>Store</a><a>Sell with us</a><a>About</a><a>Contact</a></div>
      <div class="abs links" style="left:562px;top:57px"><a>The team</a><a>Blog</a></div>
    </footer>
  </section>

  <!-- SMARTPHONE -->
  <section class="abs page m" style="left:1058px;top:96px;width:267px;height:1210px">
    <div class="photo" role="img" aria-label="Black and white portrait photo of a man" style="left:0;top:0;width:267px;height:231px;background:linear-gradient(110deg,#1a1a1a,#3a3a3a 40%,#8a8a8a 65%,#2a2a2a)"></div>
    <div class="abs brand" style="left:60px;top:100px;font-size:22px;color:#fff"><span class="brand-dot"></span>Ripper Rustic</div>
    <div class="abs blue" style="left:0;top:231px;width:267px;height:40px;display:flex;align-items:center;justify-content:center;font-size:12.5px">+ Navigation menu</div>
    <div class="abs" style="left:9px;top:296px;width:250px">
      <h3 style="font-size:14px;font-weight:700">Everything starts with an idea..</h3>
      <p style="margin-top:20px">We are Ripper Rustic and we help Australian manufacturers to sell online! Dolor sit amet, consectetur adipisicing elit, sed do eiusmod tempor incididunt ut.</p>
      <p style="margin-top:20px">Dolor sit amet, consectetur adipisicing elit, sed do eiusmod tempor incididunt ut. Dolor sit amet, consectetur adipisicing elit, sed do eiusmod tempor incididunt ut.</p>
    </div>
    <div class="photo" role="img" aria-label="Photo of a smiling woman in front of a warm striped backdrop" style="left:0;top:530px;width:267px;height:142px;background:linear-gradient(90deg,#3a1c10,#8a5a32 35%,#c08a60 70%,#6a3a22)"></div>
    <div class="abs" style="left:0;top:672px;width:267px;height:125px;background:var(--red);padding:11px 9px;color:#fff">
      <h3 style="font-size:14px;font-weight:700">Lena Marlowe starts E-commerce</h3>
      <p style="color:#fff;font-size:12px;line-height:1.25;margin-top:6px">After years of waiting Lena Marlowe finally starts her own e-commerce with the help of Ripper Rustic. She sells her own Lena Marlowe fan stuff, everything from coffee cups to t-shirts. Have a look!</p>
    </div>
    <div class="abs blue" style="left:0;top:797px;width:267px;height:166px">
      <svg class="abs" style="left:9px;top:12px" width="10" height="24"><rect x="2" y="1" width="5" height="16" rx="2.5" fill="#111"/><circle cx="4.5" cy="18" r="4.5" fill="#111"/></svg>
      <div class="abs" style="left:22px;top:7px;font-size:24px;font-weight:700;color:var(--ink)">24°</div>
      <svg class="abs" style="left:88px;top:42px" width="92" height="80" viewBox="0 0 75 65">
        <g stroke="#111" stroke-width="4" stroke-linecap="round" fill="none">
          <line x1="40" y1="4" x2="40" y2="10"/><line x1="58" y1="10" x2="54" y2="15"/><line x1="66" y1="28" x2="60" y2="28"/><line x1="22" y1="10" x2="26" y2="15"/>
          <path d="M30 24a13 13 0 0 1 23 10"/>
          <path d="M16 56h30a11 11 0 0 0 0-22 15 15 0 0 0-28 5 9 9 0 0 0-2 17z"/>
        </g>
      </svg>
      <div class="abs" style="left:0;right:0;top:134px;text-align:center;font-size:12px;color:var(--ink)"><b>Sunny,</b> a bit cloudy</div>
    </div>
    <div class="photo" role="img" aria-label="Video still of a film poster with a man's portrait" style="left:0;top:963px;width:267px;height:168px;background:linear-gradient(90deg,#0c0c0c,#2a2a2a 40%,#6b5040 70%,#2a1a1a)">
      <svg class="abs" style="left:124px;top:60px" width="26" height="28"><path d="M2 2l22 12-22 12z" fill="#fff"/></svg>
      <div class="abs" style="left:114px;top:90px;font-size:16px;font-weight:700;color:#fff">PLAY</div>
    </div>
    <div class="abs load" style="left:31px;top:1148px;width:206px;height:47px;background:linear-gradient(180deg,var(--blue),var(--blue-dark));color:#fff;font-size:16px;border-radius:2px">Load more</div>
  </section>

</div>
</body>
</html>
```